Hair salon and Nail salon in Hawaii need a newspaper Ad design.

We need a newspaper Ad design for new open hair & nail salon in Waikiki Hawaii.Our Recommendation service for hair is "Head Spa" $30+tax and for nail is "Manicure Treatment Course" (Filing+Cuticle Care+Massage+Coloring) $20+tax.
We would like to see Hawaiian taste color and also having sense of luxury design. The ad size is W 5.0” x H 6.375”.
I would customers to know the shop place(Lanakila Crest Hotel 1F) , phone(808-555-0173), instagram(salonbrightwave) , our web site https://salonbrightwave.example and recommend services. For Web or Instagram , QR code is acceptable.

Target Market(s)

women & men

Industry/Entity Type

Beauty Salon

Font styles to use
Serif

Colors

Designer to choose colors to be used in the design.

Requirements
Must have
• Tagline for local customers. Shop Name is "SALON BRIGHTWAVE".the shop place(Lanakila Crest Hotel 1F) , phone(808-555-0173), instagram(salonbrightwave) and recommend services.
Nice to have
• Our services are competitive, but we don't want to be seen as just cheap and low quality.

```html
<!DOCTYPE html>
<html lang="en">
<head>
<meta charset="utf-8">
<title>Salon Brightwave – Newspaper Ad</title>
<link rel="stylesheet" href="https://fonts.googleapis.com/css2?family=EB+Garamond:wght@400;500&family=Montserrat:wght@400;600;700&display=swap">
<style>
  :root {
    --bg-dark: #2b292b;
    --bg-mid: #4a474b;
    --footer: #121113;
    --ink-light: #ffffff;
    --ink-soft: #e9e6e6;
    --teal: #14a09a;
    --orange: #f0913f;
    --accent: #e98a3a;
    --photo-hair: #2a201c;
    --photo-skin: #8c6a5c;
  }
  * { margin: 0; padding: 0; box-sizing: border-box; }
  html, body { width: 1200px; height: 941px; overflow: hidden; background: var(--bg-dark); }
  .ad {
    position: relative;
    width: 1200px;
    height: 941px;
    overflow: hidden;
    background: radial-gradient(ellipse at 70% 35%, var(--bg-mid) 0%, #37343a 45%, var(--bg-dark) 100%);
    font-family: "Montserrat", sans-serif;
    color: var(--ink-light);
  }
  .portrait {
    position: absolute;
    left: 0; top: 0;
    width: 660px; height: 941px;
    background:
      radial-gradient(ellipse 40% 30% at 34% 45%, var(--photo-skin) 0%, rgba(140,106,92,0.35) 55%, rgba(0,0,0,0) 100%),
      linear-gradient(90deg, var(--photo-hair) 0%, #3a2d28 55%, rgba(58,45,40,0) 100%);
  }
  .brand {
    position: absolute;
    left: 641px; top: 50px;
    display: flex; align-items: center; gap: 18px;
  }
  .brand-mark { width: 104px; height: 108px; background: var(--ink-soft); }
  .brand-name { font-size: 25px; font-weight: 400; letter-spacing: 0.5px; }
  .tagline {
    position: absolute;
    left: 642px; top: 198px;
    font-family: "EB Garamond", serif;
    font-weight: 400;
    font-size: 88px;
    line-height: 88px;
    letter-spacing: 0.5px;
  }
  .services-label {
    position: absolute;
    left: 651px; top: 433px;
    font-size: 17px;
    letter-spacing: 0.3px;
  }
  .bands { position: absolute; left: 0; top: 0; }
  .service {
    position: absolute;
    font-family: "EB Garamond", serif;
    color: var(--ink-light);
  }
  .service-name { font-size: 34px; letter-spacing: 1px; line-height: 42px; }
  .service-detail { font-family: "Montserrat", sans-serif; font-size: 17px; line-height: 22px; margin-top: 2px; }
  .service--spa { left: 642px; top: 489px; }
  .service--nail { left: 648px; top: 573px; }
  .price {
    position: absolute;
    font-size: 34px;
    font-weight: 400;
  }
  .price b { font-weight: 700; }
  .price--spa { left: 995px; top: 493px; }
  .price--nail { left: 995px; top: 610px; }
  .contact {
    position: absolute;
    display: flex; align-items: center; gap: 14px;
    font-size: 27px;
    font-weight: 400;
  }
  .contact svg { flex: none; }
  .contact--address { left: 56px; top: 810px; }
  .contact--phone { left: 56px; top: 854px; }
  .contact--social { left: 536px; top: 810px; }
  .contact--web { left: 536px; top: 854px; }
  .social-dot { width: 16px; height: 16px; border-radius: 50%; background: var(--accent); margin: 0 4px 0 4px; }
</style>
</head>
<body>
<main class="ad">
  <div class="portrait" role="img" aria-label="Portrait photo of a woman with long wavy dark brown hair"></div>

  <svg class="bands" width="1200" height="941" viewBox="0 0 1200 941" aria-hidden="true">
    <defs>
      <linearGradient id="tealBand" x1="0" x2="1" y1="0" y2="0">
        <stop offset="0" stop-color="#14a09a" stop-opacity="0"/>
        <stop offset="0.35" stop-color="#14a09a" stop-opacity="0.55"/>
        <stop offset="0.7" stop-color="#14a09a"/>
        <stop offset="1" stop-color="#14a09a"/>
      </linearGradient>
      <linearGradient id="orangeBand" x1="0" x2="1" y1="0" y2="0">
        <stop offset="0" stop-color="#f0913f" stop-opacity="0"/>
        <stop offset="0.4" stop-color="#f0913f" stop-opacity="0.6"/>
        <stop offset="0.75" stop-color="#f0913f"/>
        <stop offset="1" stop-color="#f0913f"/>
      </linearGradient>
      <linearGradient id="footerFade" x1="0" x2="0" y1="0" y2="1">
        <stop offset="0" stop-color="#121113" stop-opacity="0.75"/>
        <stop offset="0.35" stop-color="#121113"/>
        <stop offset="1" stop-color="#121113"/>
      </linearGradient>
    </defs>
    <rect x="600" y="471" width="600" height="81" fill="url(#tealBand)"/>
    <path d="M600 561 H1200 V760 C1080 772 960 780 860 778 C760 776 680 770 600 764 Z" fill="url(#orangeBand)"/>
    <path d="M0 735 C220 690 430 700 640 740 C760 763 900 785 1040 780 C1110 778 1160 772 1200 766 V941 H0 Z" fill="url(#footerFade)"/>
  </svg>

  <header class="brand">
    <div class="brand-mark"></div>
    <span class="brand-name">SALON BRIGHTWAVE</span>
  </header>

  <h1 class="tagline">Quality Care<br>Quality Hair</h1>

  <p class="services-label">RECOMMENDED SERVICE</p>

  <div class="service service--spa">
    <div class="service-name">HEAD SPA</div>
  </div>
  <div class="price price--spa"><b>$30</b>+tax</div>

  <div class="service service--nail">
    <div class="service-name">MANICURE<br>TREATMENT<br>COURSE</div>
    <div class="service-detail">(Filing+Cuticle Care+Massage+Coloring)</div>
  </div>
  <div class="price price--nail"><b>$20</b>+tax</div>

  <address class="contact contact--address" style="font-style:normal">
    <svg width="20" height="24" viewBox="0 0 20 24"><path d="M10 2 C5.5 2 2.5 5.3 2.5 9.3 C2.5 14.5 10 22 10 22 C10 22 17.5 14.5 17.5 9.3 C17.5 5.3 14.5 2 10 2 Z" fill="none" stroke="#e98a3a" stroke-width="2"/><circle cx="10" cy="9.5" r="2.6" fill="none" stroke="#e98a3a" stroke-width="2"/></svg>
    <span>Lanakila Crest Hotel 1F</span>
  </address>
  <div class="contact contact--phone">
    <svg width="20" height="22" viewBox="0 0 20 22"><path d="M5 2 L8 6.5 L6 9 C7.2 11.8 9.5 14.2 12.5 15.7 L15 13.6 L19 16.8 L17 20 C9 19.5 2.5 12.8 2 4.5 Z" fill="none" stroke="#e98a3a" stroke-width="2" stroke-linejoin="round"/></svg>
    <span>808-555-0173</span>
  </div>
  <div class="contact contact--social">
    <span class="social-dot"></span>
    <span>salonbrightwave</span>
  </div>
  <div class="contact contact--web">
    <svg width="22" height="22" viewBox="0 0 22 22"><circle cx="11" cy="11" r="9" fill="none" stroke="#e98a3a" stroke-width="2"/><ellipse cx="11" cy="11" rx="4" ry="9" fill="none" stroke="#e98a3a" stroke-width="1.6"/><line x1="2" y1="11" x2="20" y2="11" stroke="#e98a3a" stroke-width="1.6"/></svg>
    <span>salonbrightwave.example</span>
  </div>
</main>
</body>
</html>
```